Values-Driven Leadership Slides

Hello. I am creating a leadership framework. I need 5 PowerPoint slides to show how my values (and sub-values) align with actions. The attached file shows the content that should be on each slide. As you will see, the first slide should be a "summary" view of all, and the four other slides should be fully readable. Please use a font available on most computers. (I envision a constellation where I can "zoom in" on individual sections, but I'm open to various concepts.)

```html
<!DOCTYPE html>
<html lang="en">
<head>
<meta charset="utf-8">
<title>Values-Driven Leadership</title>
<link href="https://fonts.googleapis.com/css2?family=Arimo:wght@400;700&display=swap" rel="stylesheet">
<style>
  :root{
    --band:#5ba3c2;
    --hub:#5ba3c2;
    --value:#c63f51;
    --action:#f7dc92;
    --edge-rose:#7b3a6e;
    --edge-violet:#5a4b8a;
    --ink:#232323;
    --white:#ffffff;
  }
  html,body{margin:0;padding:0;background:var(--white);}
  body{width:1200px;height:3369px;overflow:hidden;font-family:"Arimo",Arial,sans-serif;}
  .slide{display:block;width:1200px;height:673.8px;}
  .band{fill:var(--band);}
  .slide-title{fill:var(--white);font-weight:700;font-size:33px;text-anchor:middle;}
  .edge{stroke:var(--edge-violet);stroke-linecap:butt;}
  .overview .edge{stroke:var(--edge-violet);stroke-width:5;}
  .rose .edge{stroke:var(--edge-rose);}
  .hub{fill:var(--hub);}
  .value{fill:var(--value);}
  .action{fill:var(--action);}
  text.lbl{text-anchor:middle;dominant-baseline:central;}
  .lbl-light{fill:var(--white);}
  .lbl-dark{fill:var(--ink);}
  .bold{font-weight:700;}
</style>
</head>
<body>

<!-- Slide 1: overview -->
<svg class="slide overview" viewBox="0 0 918 516" preserveAspectRatio="none" role="img" aria-label="Values-driven leadership overview">
  <rect class="band" x="0" y="0" width="918" height="66"/>
  <text class="slide-title" x="459" y="49">Values-Driven Leadership</text>
  <g>
    <line class="edge" x1="75" y1="150" x2="164" y2="153"/>
    <line class="edge" x1="75" y1="150" x2="132" y2="258"/>
    <line class="edge" x1="75" y1="150" x2="73" y2="356"/>
    <line class="edge" x1="164" y1="153" x2="215" y2="113"/>
    <line class="edge" x1="164" y1="153" x2="274" y2="124"/>
    <line class="edge" x1="164" y1="153" x2="272" y2="189"/>
    <line class="edge" x1="164" y1="153" x2="204" y2="211"/>
    <line class="edge" x1="215" y1="113" x2="274" y2="124"/>
    <line class="edge" x1="274" y1="124" x2="272" y2="189"/>
    <line class="edge" x1="132" y1="258" x2="259" y2="276"/>
    <line class="edge" x1="132" y1="258" x2="189" y2="332"/>
    <line class="edge" x1="259" y1="276" x2="189" y2="332"/>
    <line class="edge" x1="73" y1="356" x2="215" y2="416"/>
    <line class="edge" x1="92" y1="445" x2="215" y2="416"/>

    <line class="edge" x1="348" y1="227" x2="439" y2="182"/>
    <line class="edge" x1="348" y1="227" x2="443" y2="267"/>
    <line class="edge" x1="348" y1="227" x2="352" y2="356"/>
    <line class="edge" x1="439" y1="182" x2="353" y2="136"/>
    <line class="edge" x1="439" y1="182" x2="414" y2="112"/>
    <line class="edge" x1="439" y1="182" x2="479" y2="112"/>
    <line class="edge" x1="439" y1="182" x2="531" y2="154"/>
    <line class="edge" x1="353" y1="136" x2="414" y2="112"/>
    <line class="edge" x1="479" y1="112" x2="531" y2="154"/>
    <line class="edge" x1="443" y1="267" x2="509" y2="221"/>
    <line class="edge" x1="443" y1="267" x2="548" y2="274"/>
    <line class="edge" x1="443" y1="267" x2="523" y2="335"/>
    <line class="edge" x1="443" y1="267" x2="455" y2="350"/>
    <line class="edge" x1="509" y1="221" x2="548" y2="274"/>
    <line class="edge" x1="352" y1="356" x2="333" y2="446"/>
    <line class="edge" x1="352" y1="356" x2="431" y2="445"/>
    <line class="edge" x1="352" y1="356" x2="521" y2="416"/>
    <line class="edge" x1="333" y1="446" x2="431" y2="445"/>
    <line class="edge" x1="431" y1="445" x2="521" y2="416"/>

    <line class="edge" x1="618" y1="138" x2="703" y2="127"/>
    <line class="edge" x1="703" y1="127" x2="773" y2="164"/>
    <line class="edge" x1="618" y1="138" x2="604" y2="216"/>
    <line class="edge" x1="618" y1="138" x2="685" y2="226"/>
    <line class="edge" x1="604" y1="216" x2="685" y2="226"/>
    <line class="edge" x1="773" y1="164" x2="841" y2="114"/>
    <line class="edge" x1="773" y1="164" x2="849" y2="195"/>
    <line class="edge" x1="773" y1="164" x2="780" y2="249"/>
    <line class="edge" x1="841" y1="114" x2="849" y2="195"/>
    <line class="edge" x1="849" y1="195" x2="780" y2="249"/>

    <line class="edge" x1="607" y1="326" x2="696" y2="311"/>
    <line class="edge" x1="696" y1="311" x2="775" y2="332"/>
    <line class="edge" x1="607" y1="326" x2="703" y2="391"/>
    <line class="edge" x1="607" y1="326" x2="608" y2="411"/>
    <line class="edge" x1="607" y1="326" x2="670" y2="448"/>
    <line class="edge" x1="608" y1="411" x2="670" y2="448"/>
    <line class="edge" x1="703" y1="391" x2="670" y2="448"/>
    <line class="edge" x1="775" y1="332" x2="850" y2="364"/>
    <line class="edge" x1="775" y1="332" x2="756" y2="443"/>
    <line class="edge" x1="775" y1="332" x2="835" y2="443"/>
    <line class="edge" x1="756" y1="443" x2="835" y2="443"/>
    <line class="edge" x1="850" y1="364" x2="835" y2="443"/>
  </g>
  <g font-size="9">
    <circle class="action" cx="215" cy="113" r="24"/><text class="lbl lbl-dark" x="215" y="113"><tspan x="215" dy="-0.55em">Be</tspan><tspan x="215" dy="1.1em">reliable</tspan></text>
    <circle class="action" cx="274" cy="124" r="26"/><text class="lbl lbl-dark" x="274" y="124"><tspan x="274" dy="-0.55em">Right</tspan><tspan x="274" dy="1.1em">wrongs</tspan></text>
    <circle class="action" cx="272" cy="189" r="24"/><text class="lbl lbl-dark" x="272" y="189"><tspan x="272" dy="-0.55em">Be</tspan><tspan x="272" dy="1.1em">honest</tspan></text>
    <circle class="action" cx="204" cy="211" r="33"/><text class="lbl lbl-dark" x="204" y="211"><tspan x="204" dy="-0.55em">Keep</tspan><tspan x="204" dy="1.1em">confidences</tspan></text>
    <circle class="action" cx="259" cy="276" r="40"/><text class="lbl lbl-dark" x="259" y="276" font-size="8.5"><tspan x="259" dy="-1.65em">Treat people</tspan><tspan x="259" dy="1.1em">as “human</tspan><tspan x="259" dy="1.1em">beings,” not</tspan><tspan x="259" dy="1.1em">“human doings”</tspan></text>
    <circle class="action" cx="189" cy="332" r="33"/><text class="lbl lbl-dark" x="189" y="332" font-size="8.5"><tspan x="189" dy="-1.65em">Believe that</tspan><tspan x="189" dy="1.1em">people are</tspan><tspan x="189" dy="1.1em">doing their</tspan><tspan x="189" dy="1.1em">best</tspan></text>
    <circle class="action" cx="92" cy="445" r="36"/><text class="lbl lbl-dark" x="92" y="445" font-size="8.5"><tspan x="92" dy="-1.65em">Amplify</tspan><tspan x="92" dy="1.1em">voices of</tspan><tspan x="92" dy="1.1em">marginalized</tspan><tspan x="92" dy="1.1em">people</tspan></text>
    <circle class="action" cx="215" cy="416" r="37"/><text class="lbl lbl-dark" x="215" y="416" font-size="8.5"><tspan x="215" dy="-1.65em">Co-create</tspan><tspan x="215" dy="1.1em">safe spaces</tspan><tspan x="215" dy="1.1em">for diverse</tspan><tspan x="215" dy="1.1em">groups</tspan></text>
    <circle class="hub" cx="75" cy="150" r="45"/><text class="lbl lbl-light bold" x="75" y="150" font-size="13">Connection</text>
    <circle class="value" cx="164" cy="153" r="30"/><text class="lbl lbl-light" x="164" y="153" font-size="13">Trust</text>
    <circle class="value" cx="132" cy="258" r="42"/><text class="lbl lbl-light" x="132" y="258" font-size="13">Kindness</text>
    <circle class="value" cx="73" cy="356" r="42"/><text class="lbl lbl-light" x="73" y="356" font-size="13">Inclusion</text>

    <circle class="action" cx="353" cy="136" r="25"/><text class="lbl lbl-dark" x="353" y="136"><tspan x="353" dy="-0.55em">Listen</tspan><tspan x="353" dy="1.1em">to learn</tspan></text>
    <circle class="action" cx="414" cy="112" r="30"/><text class="lbl lbl-dark" x="414" y="112" font-size="8.5"><tspan x="414" dy="-1.1em">Maintain</tspan><tspan x="414" dy="1.1em">a growth</tspan><tspan x="414" dy="1.1em">mindset</tspan></text>
    <circle class="action" cx="479" cy="112" r="27"/><text class="lbl lbl-dark" x="479" y="112"><tspan x="479" dy="-0.55em">Stay</tspan><tspan x="479" dy="1.1em">curious</tspan></text>
    <circle class="action" cx="531" cy="154" r="32"/><text class="lbl lbl-dark" x="531" y="154"><tspan x="531" dy="-1.1em">Ask</tspan><tspan x="531" dy="1.1em">excellent</tspan><tspan x="531" dy="1.1em">questions</tspan></text>
    <circle class="action" cx="509" cy="221" r="28"/><text class="lbl lbl-dark" x="509" y="221"><tspan x="509" dy="-0.55em">Try new</tspan><tspan x="509" dy="1.1em">things</tspan></text>
    <circle class="action" cx="548" cy="274" r="28"/><text class="lbl lbl-dark" x="548" y="274"><tspan x="548" dy="-1.1em">Respect</tspan><tspan x="548" dy="1.1em">pain</tspan><tspan x="548" dy="1.1em">points</tspan></text>
    <circle class="action" cx="523" cy="335" r="29"/><text class="lbl lbl-dark" x="523" y="335"><tspan x="523" dy="-0.55em">Learn from</tspan><tspan x="523" dy="1.1em">mistakes</tspan></text>
    <circle class="action" cx="455" cy="350" r="31"/><text class="lbl lbl-dark" x="455" y="350" font-size="8.5"><tspan x="455" dy="-1.65em">Choose</tspan><tspan x="455" dy="1.1em">courage</tspan><tspan x="455" dy="1.1em">over</tspan><tspan x="455" dy="1.1em">comfort</tspan></text>
    <circle class="action" cx="333" cy="446" r="29"/><text class="lbl lbl-dark" x="333" y="446"><tspan x="333" dy="-0.55em">Stay true</tspan><tspan x="333" dy="1.1em">to purpose</tspan></text>
    <circle class="action" cx="431" cy="445" r="33"/><text class="lbl lbl-dark" x="431" y="445" font-size="8"><tspan x="431" dy="-1.1em">Maintain full</tspan><tspan x="431" dy="1.1em">view of the</tspan><tspan x="431" dy="1.1em">systems</tspan></text>
    <circle class="action" cx="521" cy="416" r="31"/><text class="lbl lbl-dark" x="521" y="416"><tspan x="521" dy="-1.1em">Steward</tspan><tspan x="521" dy="1.1em">resources</tspan><tspan x="521" dy="1.1em">wisely</tspan></text>
    <circle class="hub" cx="348" cy="227" r="43"/><text class="lbl lbl-light bold" x="348" y="227" font-size="13">Growth</text>
    <circle class="value" cx="439" cy="182" r="31"/><text class="lbl lbl-light" x="439" y="182" font-size="13">Humility</text>
    <circle class="value" cx="443" cy="267" r="43"/><text class="lbl lbl-light" x="443" y="267" font-size="13">Vulnerability</text>
    <circle class="value" cx="352" cy="356" r="41"/><text class="lbl lbl-light" x="352" y="356" font-size="13">Excellence</text>

    <circle class="action" cx="841" cy="114" r="33"/><text class="lbl lbl-dark" x="841" y="114"><tspan x="841" dy="-0.55em">Disrupt</tspan><tspan x="841" dy="1.1em">oppression</tspan></text>
    <circle class="action" cx="849" cy="195" r="39"/><text class="lbl lbl-dark" x="849" y="195"><tspan x="849" dy="-1.1em">Acknowledge</tspan><tspan x="849" dy="1.1em">and challenge</tspan><tspan x="849" dy="1.1em">bias</tspan></text>
    <circle class="action" cx="780" cy="249" r="39"/><text class="lbl lbl-dark" x="780" y="249"><tspan x="780" dy="-1.65em">Center</tspan><tspan x="780" dy="1.1em">perspective</tspan><tspan x="780" dy="1.1em">of those most</tspan><tspan x="780" dy="1.1em">impacted</tspan></text>
    <circle class="action" cx="604" cy="216" r="31"/><text class="lbl lbl-dark" x="604" y="216"><tspan x="604" dy="-1.1em">Make a</tspan><tspan x="604" dy="1.1em">positive</tspan><tspan x="604" dy="1.1em">impact</tspan></text>
    <circle class="action" cx="685" cy="226" r="37"/><text class="lbl lbl-dark" x="685" y="226"><tspan x="685" dy="-1.1em">Be generous</tspan><tspan x="685" dy="1.1em">with my talent</tspan><tspan x="685" dy="1.1em">and skills</tspan></text>
    <circle class="hub" cx="703" cy="127" r="35"/><text class="lbl lbl-light bold" x="703" y="127" font-size="13">Justice</text>
    <circle class="value" cx="618" cy="138" r="31"/><text class="lbl lbl-light" x="618" y="138" font-size="13">Service</text>
    <circle class="value" cx="773" cy="164" r="29"/><text class="lbl lbl-light" x="773" y="164" font-size="13">Equity</text>

    <circle class="action" cx="703" cy="391" r="32"/><text class="lbl lbl-dark" x="703" y="391"><tspan x="703" dy="-0.55em">Commit to</tspan><tspan x="703" dy="1.1em">authenticity</tspan></text>
    <circle class="action" cx="608" cy="411" r="35"/><text class="lbl lbl-dark" x="608" y="411"><tspan x="608" dy="-0.55em">Practice</tspan><tspan x="608" dy="1.1em">mindfulness</tspan></text>
    <circle class="action" cx="670" cy="448" r="29"/><text class="lbl lbl-dark" x="670" y="448"><tspan x="670" dy="-0.55em">Model</tspan><tspan x="670" dy="1.1em">self-love</tspan></text>
    <circle class="action" cx="850" cy="364" r="39"/><text class="lbl lbl-dark" x="850" y="364"><tspan x="850" dy="-1.1em">Express</tspan><tspan x="850" dy="1.1em">genuine</tspan><tspan x="850" dy="1.1em">appreciation</tspan></text>
    <circle class="action" cx="756" cy="443" r="29"/><text class="lbl lbl-dark" x="756" y="443"><tspan x="756" dy="-0.55em">Nurture</tspan><tspan x="756" dy="1.1em">optimism</tspan></text>
    <circle class="action" cx="835" cy="443" r="32"/><text class="lbl lbl-dark" x="835" y="443"><tspan x="835" dy="-1.1em">Seek the</tspan><tspan x="835" dy="1.1em">silver</tspan><tspan x="835" dy="1.1em">linings</tspan></text>
    <circle class="hub" cx="696" cy="311" r="37"/><text class="lbl lbl-light bold" x="696" y="311" font-size="13">Joy</text>
    <circle class="value" cx="607" cy="326" r="30"/><text class="lbl lbl-light" x="607" y="326" font-size="13">Health</text>
    <circle class="value" cx="775" cy="332" r="33"/><text class="lbl lbl-light" x="775" y="332" font-size="13">Gratitude</text>
  </g>
</svg>

<!-- Slide 2: Connection -->
<svg class="slide rose" viewBox="0 0 918 516" preserveAspectRatio="none" role="img" aria-label="Connection values map">
  <rect class="band" x="0" y="0" width="918" height="66"/>
  <text class="slide-title" x="459" y="49">Value-Driven Leadership</text>
  <g stroke-width="7">
    <line class="edge" x1="518" y1="196" x2="283" y2="251" stroke-width="13"/>
    <line class="edge" x1="518" y1="196" x2="411" y2="345" stroke-width="13"/>
    <line class="edge" x1="518" y1="196" x2="716" y2="288" stroke-width="13"/>
    <line class="edge" x1="283" y1="251" x2="100" y2="172"/>
    <line class="edge" x1="283" y1="251" x2="203" y2="121"/>
    <line class="edge" x1="283" y1="251" x2="330" y2="129"/>
    <line class="edge" x1="283" y1="251" x2="122" y2="283"/>
    <line class="edge" x1="100" y1="172" x2="203" y2="121"/>
    <line class="edge" x1="203" y1="121" x2="330" y2="129"/>
    <line class="edge" x1="100" y1="172" x2="122" y2="283"/>
    <line class="edge" x1="411" y1="345" x2="240" y2="389"/>
    <line class="edge" x1="411" y1="345" x2="544" y2="440"/>
    <line class="edge" x1="240" y1="389" x2="544" y2="440"/>
    <line class="edge" x1="716" y1="288" x2="795" y2="165"/>
    <line class="edge" x1="716" y1="288" x2="819" y2="388"/>
    <line class="edge" x1="795" y1="165" x2="819" y2="388"/>
  </g>
  <g font-size="14.5">
    <circle class="action" cx="100" cy="172" r="40"/><text class="lbl lbl-dark" x="100" y="172"><tspan x="100" dy="-0.55em">Be</tspan><tspan x="100" dy="1.1em">honest</tspan></text>
    <circle class="action" cx="203" cy="121" r="40"/><text class="lbl lbl-dark" x="203" y="121"><tspan x="203" dy="-0.55em">Right</tspan><tspan x="203" dy="1.1em">wrongs</tspan></text>
    <circle class="action" cx="330" cy="129" r="50"/><text class="lbl lbl-dark" x="330" y="129"><tspan x="330" dy="-0.55em">Keep</tspan><tspan x="330" dy="1.1em">confidences</tspan></text>
    <circle class="action" cx="122" cy="283" r="38"/><text class="lbl lbl-dark" x="122" y="283"><tspan x="122" dy="-0.55em">Be</tspan><tspan x="122" dy="1.1em">reliable</tspan></text>
    <circle class="action" cx="240" cy="389" r="66"/><text class="lbl lbl-dark" x="240" y="389"><tspan x="240" dy="-1.65em">Treat people as</tspan><tspan x="240" dy="1.1em">“human beings,”</tspan><tspan x="240" dy="1.1em">not “human</tspan><tspan x="240" dy="1.1em">doing”</tspan></text>
    <circle class="action" cx="544" cy="440" r="56"/><text class="lbl lbl-dark" x="544" y="440"><tspan x="544" dy="-1.65em">Believe that</tspan><tspan x="544" dy="1.1em">people are</tspan><tspan x="544" dy="1.1em">doing their</tspan><tspan x="544" dy="1.1em">best</tspan></text>
    <circle class="action" cx="795" cy="165" r="56"/><text class="lbl lbl-dark" x="795" y="165"><tspan x="795" dy="-1.1em">Amplify voices</tspan><tspan x="795" dy="1.1em">of marginalized</tspan><tspan x="795" dy="1.1em">people</tspan></text>
    <circle class="action" cx="819" cy="388" r="52"/><text class="lbl lbl-dark" x="819" y="388"><tspan x="819" dy="-1.65em">Co-create</tspan><tspan x="819" dy="1.1em">safe spaces</tspan><tspan x="819" dy="1.1em">for diverse</tspan><tspan x="819" dy="1.1em">groups</tspan></text>
    <circle class="hub" cx="518" cy="196" r="104"/><text class="lbl lbl-light bold" x="518" y="196" font-size="32">Connection</text>
    <circle class="value" cx="283" cy="251" r="51"/><text class="lbl lbl-light bold" x="283" y="251" font-size="18">Trust</text>
    <circle class="value" cx="411" cy="345" r="56"/><text class="lbl lbl-light bold" x="411" y="345" font-size="18">Kindness</text>
    <circle class="value" cx="716" cy="288" r="55"/><text class="lbl lbl-light bold" x="716" y="288" font-size="18">Inclusion</text>
  </g>
</svg>

<!-- Slide 3: Growth -->
<svg class="slide" viewBox="0 0 918 516" preserveAspectRatio="none" role="img" aria-label="Growth values map">
  <rect class="band" x="0" y="0" width="918" height="66"/>
  <text class="slide-title" x="459" y="49">Values-Driven Leadership</text>
  <g stroke-width="7">
    <line class="edge" x1="259" y1="165" x2="648" y2="134" stroke-width="12"/>
    <line class="edge" x1="259" y1="165" x2="476" y2="253" stroke-width="12"/>
    <line class="edge" x1="259" y1="165" x2="207" y2="335" stroke-width="12"/>
    <line class="edge" x1="648" y1="134" x2="796" y2="135"/>
    <line class="edge" x1="648" y1="134" x2="835" y2="261"/>
    <line class="edge" x1="648" y1="134" x2="721" y2="280"/>
    <line class="edge" x1="796" y1="135" x2="835" y2="261"/>
    <line class="edge" x1="721" y1="280" x2="835" y2="261"/>
    <line class="edge" x1="476" y1="253" x2="602" y2="253"/>
    <line class="edge" x1="476" y1="253" x2="369" y2="315"/>
    <line class="edge" x1="476" y1="253" x2="456" y2="354"/>
    <line class="edge" x1="476" y1="253" x2="565" y2="362"/>
    <line class="edge" x1="369" y1="315" x2="456" y2="354"/>
    <line class="edge" x1="456" y1="354" x2="565" y2="362"/>
    <line class="edge" x1="565" y1="362" x2="602" y2="253"/>
    <line class="edge" x1="207" y1="335" x2="101" y2="272"/>
    <line class="edge" x1="207" y1="335" x2="91" y2="388"/>
    <line class="edge" x1="207" y1="335" x2="174" y2="441"/>
    <line class="edge" x1="207" y1="335" x2="283" y2="417"/>
    <line class="edge" x1="101" y1="272" x2="91" y2="388"/>
    <line class="edge" x1="91" y1="388" x2="174" y2="441"/>
    <line class="edge" x1="174" y1="441" x2="283" y2="417"/>
  </g>
  <g font-size="14.5">
    <circle class="action" cx="796" cy="135" r="50"/><text class="lbl lbl-dark" x="796" y="135"><tspan x="796" dy="-0.55em">Stay true</tspan><tspan x="796" dy="1.1em">to purpose</tspan></text>
    <circle class="action" cx="835" cy="261" r="53"/><text class="lbl lbl-dark" x="835" y="261"><tspan x="835" dy="-1.65em">Maintain</tspan><tspan x="835" dy="1.1em">full view</tspan><tspan x="835" dy="1.1em">of the</tspan><tspan x="835" dy="1.1em">systems</tspan></text>
    <circle class="action" cx="721" cy="280" r="45"/><text class="lbl lbl-dark" x="721" y="280"><tspan x="721" dy="-1.1em">Steward</tspan><tspan x="721" dy="1.1em">resources</tspan><tspan x="721" dy="1.1em">wisely</tspan></text>
    <circle class="action" cx="602" cy="253" r="50"/><text class="lbl lbl-dark" x="602" y="253"><tspan x="602" dy="-1.1em">Choose</tspan><tspan x="602" dy="1.1em">courage over</tspan><tspan x="602" dy="1.1em">comfort</tspan></text>
    <circle class="action" cx="369" cy="315" r="44"/><text class="lbl lbl-dark" x="369" y="315"><tspan x="369" dy="-0.55em">Try new</tspan><tspan x="369" dy="1.1em">things</tspan></text>
    <circle class="action" cx="456" cy="354" r="45"/><text class="lbl lbl-dark" x="456" y="354"><tspan x="456" dy="-0.55em">Respect</tspan><tspan x="456" dy="1.1em">pain points</tspan></text>
    <circle class="action" cx="565" cy="362" r="48"/><text class="lbl lbl-dark" x="565" y="362"><tspan x="565" dy="-0.55em">Learn from</tspan><tspan x="565" dy="1.1em">mistakes</tspan></text>
    <circle class="action" cx="101" cy="272" r="44"/><text class="lbl lbl-dark" x="101" y="272"><tspan x="101" dy="-0.55em">Listen</tspan><tspan x="101" dy="1.1em">to learn</tspan></text>
    <circle class="action" cx="91" cy="388" r="45"/><text class="lbl lbl-dark" x="91" y="388"><tspan x="91" dy="-1.1em">Maintain</tspan><tspan x="91" dy="1.1em">a growth</tspan><tspan x="91" dy="1.1em">mindset</tspan></text>
    <circle class="action" cx="174" cy="441" r="40"/><text class="lbl lbl-dark" x="174" y="441"><tspan x="174" dy="-0.55em">Stay</tspan><tspan x="174" dy="1.1em">curious</tspan></text>
    <circle class="action" cx="283" cy="417" r="49"/><text class="lbl lbl-dark" x="283" y="417"><tspan x="283" dy="-1.1em">Ask</tspan><tspan x="283" dy="1.1em">excellent</tspan><tspan x="283" dy="1.1em">questions</tspan></text>
    <circle class="hub" cx="259" cy="165" r="84"/><text class="lbl lbl-light bold" x="259" y="165" font-size="32">Growth</text>
    <circle class="value" cx="648" cy="134" r="55"/><text class="lbl lbl-light bold" x="648" y="134" font-size="18">Excellence</text>
    <circle class="value" cx="476" cy="253" r="64"/><text class="lbl lbl-light bold" x="476" y="253" font-size="18">Vulnerability</text>
    <circle class="value" cx="207" cy="335" r="50"/><text class="lbl lbl-light bold" x="207" y="335" font-size="18">Humility</text>
  </g>
</svg>

<!-- Slide 4: Justice -->
<svg class="slide" viewBox="0 0 918 516" preserveAspectRatio="none" role="img" aria-label="Justice values map">
  <rect class="band" x="0" y="0" width="918" height="66"/>
  <text class="slide-title" x="459" y="49">Values-Driven Leadership</text>
  <g stroke-width="7">
    <line class="edge" x1="255" y1="190" x2="624" y2="192" stroke-width="13"/>
    <line class="edge" x1="255" y1="190" x2="162" y2="331"/>
    <line class="edge" x1="255" y1="190" x2="307" y2="380"/>
    <line class="edge" x1="162" y1="331" x2="307" y2="380"/>
    <line class="edge" x1="624" y1="192" x2="535" y2="359"/>
    <line class="edge" x1="624" y1="192" x2="746" y2="316" stroke-width="10"/>
    <line class="edge" x1="535" y1="359" x2="658" y2="411"/>
    <line class="edge" x1="658" y1="411" x2="746" y2="316"/>
  </g>
  <g font-size="14.5">
    <circle class="action" cx="162" cy="331" r="47"/><text class="lbl lbl-dark" x="162" y="331"><tspan x="162" dy="-1.1em">Make a</tspan><tspan x="162" dy="1.1em">positive</tspan><tspan x="162" dy="1.1em">impact</tspan></text>
    <circle class="action" cx="307" cy="380" r="57"/><text class="lbl lbl-dark" x="307" y="380"><tspan x="307" dy="-1.1em">Be generous</tspan><tspan x="307" dy="1.1em">with my talent</tspan><tspan x="307" dy="1.1em">and skills</tspan></text>
    <circle class="action" cx="535" cy="359" r="47"/><text class="lbl lbl-dark" x="535" y="359"><tspan x="535" dy="-0.55em">Disrupt</tspan><tspan x="535" dy="1.1em">oppression</tspan></text>
    <circle class="action" cx="658" cy="411" r="56"/><text class="lbl lbl-dark" x="658" y="411"><tspan x="658" dy="-1.1em">Acknowledge</tspan><tspan x="658" dy="1.1em">and challenge</tspan><tspan x="658" dy="1.1em">bias</tspan></text>
    <circle class="action" cx="746" cy="316" r="56"/><text class="lbl lbl-dark" x="746" y="316"><tspan x="746" dy="-1.65em">Center</tspan><tspan x="746" dy="1.1em">perspective</tspan><tspan x="746" dy="1.1em">of those most</tspan><tspan x="746" dy="1.1em">impacted</tspan></text>
    <circle class="hub" cx="446" cy="188" r="84"/><text class="lbl lbl-light bold" x="446" y="188" font-size="32">Justice</text>
    <circle class="value" cx="255" cy="190" r="49"/><text class="lbl lbl-light" x="255" y="190" font-size="18">Service</text>
    <circle class="value" cx="624" cy="192" r="50"/><text class="lbl lbl-light" x="624" y="192" font-size="18">Equity</text>
  </g>
</svg>

<!-- Slide 5: Joy -->
<svg class="slide" viewBox="0 0 918 516" preserveAspectRatio="none" role="img" aria-label="Joy values map">
  <rect class="band" x="0" y="0" width="918" height="66"/>
  <text class="slide-title" x="459" y="49">Values-Driven Leadership</text>
  <g stroke-width="7">
    <line class="edge" x1="209" y1="197" x2="614" y2="231" stroke-width="13"/>
    <line class="edge" x1="209" y1="197" x2="117" y2="350"/>
    <line class="edge" x1="209" y1="197" x2="238" y2="419"/>
    <line class="edge" x1="209" y1="197" x2="371" y2="350"/>
    <line class="edge" x1="117" y1="350" x2="238" y2="419"/>
    <line class="edge" x1="238" y1="419" x2="371" y2="350"/>
    <line class="edge" x1="614" y1="231" x2="758" y2="160"/>
    <line class="edge" x1="614" y1="231" x2="805" y2="314"/>
    <line class="edge" x1="614" y1="231" x2="626" y2="397"/>
    <line class="edge" x1="758" y1="160" x2="805" y2="314"/>
    <line class="edge" x1="805" y1="314" x2="626" y2="397"/>
  </g>
  <g font-size="14.5">
    <circle class="action" cx="117" cy="350" r="61"/><text class="lbl lbl-dark" x="117" y="350"><tspan x="117" dy="-0.55em">Practice</tspan><tspan x="117" dy="1.1em">mindfulness</tspan></text>
    <circle class="action" cx="238" cy="419" r="54"/><text class="lbl lbl-dark" x="238" y="419"><tspan x="238" dy="-0.55em">Model</tspan><tspan x="238" dy="1.1em">self-love</tspan></text>
    <circle class="action" cx="371" cy="350" r="58"/><text class="lbl lbl-dark" x="371" y="350"><tspan x="371" dy="-0.55em">Commit to</tspan><tspan x="371" dy="1.1em">authenticity</tspan></text>
    <circle class="action" cx="758" cy="160" r="52"/><text class="lbl lbl-dark" x="758" y="160"><tspan x="758" dy="-0.55em">Nurture</tspan><tspan x="758" dy="1.1em">optimism</tspan></text>
    <circle class="action" cx="805" cy="314" r="54"/><text class="lbl lbl-dark" x="805" y="314"><tspan x="805" dy="-0.55em">Seek the</tspan><tspan x="805" dy="1.1em">silver linings</tspan></text>
    <circle class="action" cx="626" cy="397" r="60"/><text class="lbl lbl-dark" x="626" y="397"><tspan x="626" dy="-1.1em">Express</tspan><tspan x="626" dy="1.1em">genuine</tspan><tspan x="626" dy="1.1em">appreciation</tspan></text>
    <circle class="hub" cx="431" cy="177" r="79"/><text class="lbl lbl-light bold" x="431" y="177" font-size="32">Joy</text>
    <circle class="value" cx="209" cy="197" r="61"/><text class="lbl lbl-light" x="209" y="197" font-size="18">Health</text>
    <circle class="value" cx="614" cy="231" r="61"/><text class="lbl lbl-light" x="614" y="231" font-size="18">Gratitude</text>
  </g>
</svg>

</body>
</html>
```